Cover for a Non-Fiction Book on Authoritarianism for a Washington D.C. Think Tank

Create a dynamic and engaging cover highlighting the role of contemporary and historical authoritarianism for a non-fiction edited volume. The book brings together chapters from many leading academics on the subject. The tone should be serious but provocative. Proprietary images are not acceptable as we are not budgeting for licensing. The books dimensions are 6x9. Preference will be given to designers with front and back cover design with sample ipsum lorum text.

One of covers that we particularly liked was "How Quiet Defiance Endures" a link to the image on shelvoria is: http://www.shelvoria-books.example/s/ref=nb_sb_noss/482-7715093-6620841?url=search-alias%3Daps&field-keywords=How+Quiet+Defiance+Endures

Attached is a draft version of the manuscript to assist in shaping your creative vision.

Project Deadline Extended Reason: I have extended the deadline at the request of the editors. They would like to see some designs that rely less heavily on the themes of fists and barbed wire to reference authoritarianism. I apologize to designs with current submissions, some of them are very professional, however none of the designs are currently under consideration for use. Added Saturday, January 24, 2015

Project Deadline Extended Reason: Editors are still unsatisfied with current sample of options. I apologize to those current contributors, but anything challenging and new would be well received. Added Friday, January 30, 2015

Project Deadline Extended Reason: I've updated the deadline so that designers that were well ranked can submit full front and back covers to assist the book editors in making their final decision. Added Friday, February 13, 2015

Font styles to use
Serif
Sans Serif

Requirements
Must have
• 1) Title: Are Strongmen Regaining the Upper Ground
• 2) Editors: Tobias Lindqvern and Elena K. Marwood
• 3) Language from client: "a simple design that captured both a symbol of repression and resistance would be ideal. The cover of How Quiet Defiance Endures is a great example. Nothing busy or overly complicated. The image of mass street protests may be overused at this point so I'd opt for something a bit more creative. Vibrant colors always great."
• 4) This final project design must use the attached InDesign template file when constructing the cover (IDML and INDD versions of the template are available).
Nice to have
• Feel free to use Harborline Forum logo designs pulled from the web.
Should not have
• Photographs that would require compensating a copyright holder.

```html
<!DOCTYPE html>
<html lang="en">
<head>
<meta charset="utf-8">
<title>Are Strongmen Regaining the Upper Ground? — Book Cover</title>
<link rel="stylesheet" href="https://fonts.googleapis.com/css2?family=Source+Sans+3:wght@400&family=EB+Garamond:wght@500&display=swap">
<style>
  :root {
    --ink-black: #000000;
    --cover-white: #ffffff;
    --signal-red: #d0232a;
    --deep-red: #9e1419;
    --title-grey: #f2f2f2;
    --editor-grey: #3a3a3a;
  }
  html, body {
    margin: 0;
    padding: 0;
    width: 800px;
    height: 1200px;
    overflow: hidden;
    background: var(--cover-white);
  }
  .cover {
    position: relative;
    width: 800px;
    height: 1200px;
    background: var(--cover-white);
  }
  .cover__field {
    position: absolute;
    left: 0;
    top: 0;
    width: 800px;
    height: 1008px;
    background: var(--ink-black);
  }
  .cover__title {
    position: absolute;
    left: 58px;
    top: 26px;
    margin: 0;
    font-family: "Source Sans 3", "Helvetica Neue", Arial, sans-serif;
    font-weight: 400;
    font-size: 40px;
    line-height: 48px;
    color: var(--title-grey);
    letter-spacing: 0.2px;
  }
  .cover__emblem {
    position: absolute;
    left: 230px;
    top: 235px;
    width: 400px;
    height: 690px;
    border-radius: 46% 46% 30% 30%;
    background: radial-gradient(ellipse at 55% 35%, var(--signal-red) 0%, var(--deep-red) 55%, rgba(158, 20, 25, 0) 72%);
  }
  .cover__rule {
    position: absolute;
    left: 0;
    top: 1008px;
    width: 800px;
    height: 14px;
    background: var(--signal-red);
  }
  .cover__editors {
    position: absolute;
    left: 0;
    top: 1108px;
    width: 800px;
    margin: 0;
    text-align: center;
    font-family: "EB Garamond", Garamond, "Times New Roman", serif;
    font-weight: 500;
    font-size: 36px;
    font-variant: small-caps;
    letter-spacing: 3px;
    color: var(--editor-grey);
  }
</style>
</head>
<body>
  <main class="cover">
    <section class="cover__field">
      <h1 class="cover__title">Are Strongmen Regaining<br>the Upper Ground?</h1>
      <div class="cover__emblem" role="img" aria-label="Red painted raised fist with dripping paint streaks below the wrist"></div>
    </section>
    <div class="cover__rule"></div>
    <p class="cover__editors">Tobias Lindqvern and Elena K. Marwood</p>
  </main>
</body>
</html>
```